Business Card Design Project

Use our current logo. Clean design.

Industry/Entity Type

Business

Requirements
Must have
• Marisela DUBRANCQ
M. Law
Managing Partner

Alpenvorsa AG
Kornhalmweg 214
CH-3097 Liebefeld

M. +41 79 412 56 27
T. +41 31 928 44 10
F. +41 31 928 44 19

m.dubrancq@alpenvorsa-example.com
www.alpenvorsa-example.com

```html
<!DOCTYPE html>
<html lang="en">
<head>
<meta charset="utf-8">
<title>Alpenvorsa – Business Card</title>
<link rel="stylesheet" href="https://fonts.googleapis.com/css2?family=Source+Sans+3:wght@400;600&display=swap">
<style>
  :root {
    --backdrop: #262424;
    --card-white: #ffffff;
    --card-dark: #2f2b2a;
    --taupe: #7a716a;
    --sage: #9ea196;
    --text-dark: #4a4544;
    --text-label: #8a8580;
    --text-light: #b8b1aa;
  }
  * { margin: 0; padding: 0; box-sizing: border-box; }
  html, body {
    width: 1200px; height: 515px; overflow: hidden;
    background: var(--backdrop);
    font-family: "Source Sans 3", "Myriad Pro", Arial, sans-serif;
  }
  .canvas { position: relative; width: 1200px; height: 515px; }
  .card {
    position: absolute; width: 512px; height: 306px; overflow: hidden;
  }
  .card--front { left: 48px; top: 36px; background: var(--card-white); }
  .card--back { left: 600px; top: 154px; background: var(--card-dark); }
  .card__facets { position: absolute; inset: 0; width: 100%; height: 100%; }
  .facet--band { fill: var(--sage); }
  .facet--fill { fill: var(--taupe); }

  .brand {
    position: absolute; left: 36px;
    font-size: 27px; font-weight: 400; letter-spacing: 0.04em;
    text-transform: uppercase; line-height: 1;
  }
  .card--front .brand { top: 104px; color: var(--taupe); }
  .card--back .brand { top: 96px; color: var(--text-light); }

  .contact {
    position: absolute; left: 42px; top: 204px;
    display: flex; font-size: 10.5px; line-height: 13.5px; color: var(--text-dark);
  }
  .contact__col { padding-right: 12px; }
  .contact__col + .contact__col {
    padding-left: 12px; border-left: 1px solid var(--text-label);
  }
  .contact__label { color: var(--text-label); text-transform: uppercase; }

  .person {
    position: absolute; left: 42px; top: 194px;
    font-size: 10.5px; line-height: 13.5px; color: var(--text-light);
  }
</style>
</head>
<body>
<main class="canvas">

  <section class="card card--front" aria-label="Card front">
    <svg class="card__facets" viewBox="0 0 427 255" preserveAspectRatio="none" aria-hidden="true">
      <polygon class="facet--band" points="340,0 427,0 427,87"/>
      <polygon class="facet--fill" points="357,0 427,0 427,70"/>
      <polygon class="facet--band" points="275,255 427,103 427,255"/>
      <polygon class="facet--fill" points="293,255 427,121 427,255"/>
    </svg>
    <div class="brand">Alpenvorsa</div>
    <div class="contact">
      <div class="contact__col">
        <div class="contact__label">Adress</div>
        <div>Alpenvorsa AG</div>
        <div>Kornhalmweg 214</div>
        <div>CH-3097 Liebefeld</div>
      </div>
      <div class="contact__col">
        <div class="contact__label">Phone</div>
        <div>M. +41 79 412 56 27</div>
        <div>T. +41 31 928 44 10</div>
        <div>F. +41 31 928 44 19</div>
      </div>
    </div>
  </section>

  <section class="card card--back" aria-label="Card back">
    <svg class="card__facets" viewBox="0 0 427 255" preserveAspectRatio="none" aria-hidden="true">
      <polygon class="facet--band" points="340,0 427,0 427,87"/>
      <polygon class="facet--fill" points="357,0 427,0 427,70"/>
      <polygon class="facet--band" points="275,255 427,103 427,255"/>
      <polygon class="facet--fill" points="293,255 427,121 427,255"/>
    </svg>
    <div class="brand">Alpenvorsa</div>
    <div class="person">
      <div>Marisela DUBRANCQ</div>
      <div>M. Law</div>
      <div>Managing Partner</div>
      <div>m.dubrancq@alpenvorsa-example.com</div>
      <div>www.alpenvorsa-example.com</div>
    </div>
  </section>

</main>
</body>
</html>
```